'Marlow Ridge' wine label

We are looking to create a new wine brand called "Marlow Ridge."

We have no preconceived notions about color, design or otherwise. This design should be incorporated into a wine label that will ultimately be affixed to either a 750ml bottle or a wine box. We've attached some images of wine label artwork and bottle shots - but yours does NOT need to look like these - they're there just for illustration purposes.

Target Market(s)

Target market for this wine brand will be "broad market" retail - i.e., big box stores, wine shops, etc.

Logo Text

Marlow Ridge

```html
<!DOCTYPE html>
<html lang="en">
<head>
<meta charset="utf-8">
<title>Marlow Ridge — Wine Label Concepts</title>
<link rel="stylesheet" href="https://fonts.googleapis.com/css2?family=Della+Respira&family=PT+Sans:wght@400;700&family=Libre+Baskerville&display=swap">
<style>
  :root {
    --paper: #ffffff;
    --ink: #111111;
    --berry: #b3185c;
    --berry-soft: #e7a8c3;
    --berry-pale: #f8e3ec;
    --grey: #8a8a8a;
    --grey-light: #c4c4c4;
    --frame-dark: #555555;
    --frame-pink: #c97a9c;
  }
  html, body {
    margin: 0;
    padding: 0;
    width: 1200px;
    height: 718px;
    overflow: hidden;
    background: var(--paper);
  }
  .sheet { display: block; width: 1200px; height: 718px; }
  .label-frame { fill: none; stroke-width: 1.3; }
  .label-frame--classic { stroke: var(--frame-dark); }
  .label-frame--engraved { stroke: var(--frame-pink); }
  .emblem-oval { fill: var(--berry); }
  .brand-name {
    font-family: "Della Respira", "Times New Roman", serif;
    font-size: 72px;
    fill: var(--ink);
    text-anchor: middle;
  }
  .wine-type {
    font-family: "PT Sans", Arial, sans-serif;
    font-weight: 700;
    font-size: 18px;
    letter-spacing: 2.5px;
    fill: var(--berry);
    text-anchor: middle;
  }
  .vintage {
    font-family: "Libre Baskerville", Georgia, serif;
    fill: var(--grey);
    text-anchor: middle;
  }
  .vintage--large { font-size: 27px; }
  .vintage--small { font-size: 22px; }
  .maker {
    font-family: "PT Sans", Arial, sans-serif;
    fill: var(--ink);
    text-anchor: middle;
    letter-spacing: 0.5px;
  }
  .maker--large { font-size: 23px; }
  .maker--small { font-size: 20px; }
  .legal {
    font-family: "PT Sans", Arial, sans-serif;
    font-size: 17px;
    fill: var(--ink);
  }
  .legal--right { text-anchor: end; }
  .flourish { fill: var(--grey); }
  .flourish--light { fill: var(--grey-light); }
</style>
</head>
<body>
<svg class="sheet" viewBox="0 0 1200 718" xmlns="http://www.w3.org/2000/svg">
  <defs>
    <linearGradient id="engraving-tone" x1="0" y1="0" x2="0" y2="1">
      <stop offset="0" stop-color="var(--berry-pale)"/>
      <stop offset="1" stop-color="var(--berry-soft)"/>
    </linearGradient>
  </defs>

  <!-- Classic label -->
  <g class="label label--classic">
    <rect class="label-frame label-frame--classic" x="3" y="3" width="560" height="712"/>
    <ellipse class="emblem-oval" cx="281" cy="135" rx="143" ry="89" role="img" aria-label="Engraved mountain peak with clouds inside an oval"/>
    <text class="brand-name" x="281" y="330">Marlow Ridge</text>
    <text class="wine-type" x="281" y="371">RED WINE</text>
    <rect class="flourish" x="200" y="425" width="30" height="3" rx="1.5" role="img" aria-label="Small flourish"/>
    <text class="vintage vintage--large" x="281" y="437">2006</text>
    <rect class="flourish" x="332" y="425" width="30" height="3" rx="1.5" role="img" aria-label="Small flourish"/>
    <text class="maker maker--large" x="281" y="502">VINTED &amp; BOTTLED BY</text>
    <text class="maker maker--large" x="281" y="552">MARLOW RIDGE WINERY • MELBOURNE, AU</text>
    <text class="legal" x="16" y="698">Alc. 12%  By Vol.</text>
    <text class="legal legal--right" x="548" y="698">750 ml</text>
  </g>

  <!-- Engraved label -->
  <g class="label label--engraved">
    <rect class="label-frame label-frame--engraved" x="635" y="3" width="561" height="712"/>
    <rect x="735" y="56" width="364" height="192" rx="40" fill="url(#engraving-tone)" role="img" aria-label="Engraved mountain peak with clouds and rolling hills"/>
    <text class="brand-name" x="915" y="326">Marlow Ridge</text>
    <rect class="flourish flourish--light" x="763" y="383" width="311" height="4" rx="2" role="img" aria-label="Decorative scroll divider"/>
    <text class="wine-type" x="915" y="429">RED WINE</text>
    <rect class="flourish flourish--light" x="844" y="463" width="32" height="3" rx="1.5" role="img" aria-label="Small flourish"/>
    <text class="vintage vintage--small" x="915" y="473">2006</text>
    <rect class="flourish flourish--light" x="954" y="463" width="32" height="3" rx="1.5" role="img" aria-label="Small flourish"/>
    <text class="maker maker--small" x="915" y="533">VINTED &amp; BOTTLED BY</text>
    <text class="maker maker--small" x="915" y="574">MARLOW RIDGE WINERY • MELBOURNE, AU</text>
    <text class="legal" x="651" y="698">Alc. 12%  By Vol.</text>
    <text class="legal legal--right" x="1183" y="698">750 ml</text>
  </g>
</svg>
</body>
</html>
```